Business Card Design

Hoping for a black background business card, minimalistic design.
With the Marble Crest logo you created in white.

I would like to include:
My Name and title
Address (street address)
Reception: (phone number)
Fax: (fax number)
Reception: (email address)
Direct email: (email address)
Instagram: (ig handle)

```html
<!DOCTYPE html>
<html lang="en">
<head>
<meta charset="utf-8">
<title>Marble Crest Business Card</title>
<link href="https://fonts.googleapis.com/css2?family=Open+Sans:wght@400;600;700&display=swap" rel="stylesheet">
<style>
  :root{
    --backdrop:#3b3b3b;
    --card:#111111;
    --card-edge:#1c1c1c;
    --ink:#ffffff;
    --ink-soft:#cfcfcf;
    --ink-muted:#8a8a8a;
    --rule:#9a9a9a;
    --pattern-a:#141414;
    --pattern-b:#262626;
  }
  *{box-sizing:border-box;margin:0;padding:0}
  html,body{width:1200px;height:801px;overflow:hidden}
  body{
    background:var(--backdrop);
    font-family:"Open Sans",Arial,sans-serif;
    color:var(--ink);
    position:relative;
  }
  .card{
    position:absolute;
    width:525px;height:300px;
    background:var(--card);
    border:1px solid var(--card-edge);
    box-shadow:0 10px 30px rgba(0,0,0,.35);
  }
  .card--front{left:50px;top:250px}
  .card--back{left:625px;top:250px;overflow:hidden}

  .brand{
    position:absolute;
    display:flex;align-items:center;gap:12px;
    white-space:nowrap;
  }
  .brand__mark{
    width:40px;height:40px;border:2px solid var(--ink);border-radius:50%;flex:none;
  }
  .brand__rule{width:1px;height:42px;background:var(--rule);flex:none}
  .brand__name{
    font-size:19px;font-weight:400;letter-spacing:3px;text-transform:uppercase;
  }
  .card--front .brand{left:28px;top:190px;gap:10px}
  .card--front .brand__name{font-size:16px;letter-spacing:2px}

  .front__divider{
    position:absolute;left:272px;top:40px;width:1px;height:220px;background:var(--rule);
  }
  .details{position:absolute;left:290px;top:42px;right:14px}
  .details__name{font-size:17px;font-weight:700;letter-spacing:.5px;text-transform:uppercase}
  .details__title{font-size:12px;color:var(--ink-soft);margin-bottom:12px}
  .details__address{font-size:12px;line-height:1.45;margin-bottom:12px}
  .contacts{list-style:none;font-size:12px;line-height:1.6}
  .contacts li{display:flex;align-items:center;gap:7px;white-space:nowrap}
  .contacts svg{width:11px;height:11px;flex:none;fill:var(--ink)}
  .contacts__label{font-size:9px;color:var(--ink-muted)}

  .back__pattern{
    position:absolute;inset:0;
    background:linear-gradient(120deg,var(--pattern-a) 0%,var(--pattern-b) 55%,var(--pattern-a) 100%);
  }
  .card--back .brand{left:150px;top:128px;background:var(--card);padding:8px 14px}
</style>
</head>
<body>

<section class="card card--front" aria-label="Card front">
  <div class="brand">
    <span class="brand__mark"></span>
    <span class="brand__rule"></span>
    <span class="brand__name">Marble Crest</span>
  </div>
  <span class="front__divider"></span>
  <div class="details">
    <p class="details__name">Daniel Reyes</p>
    <p class="details__title">President</p>
    <p class="details__address">418 Harbor Lane, Suite 210<br>Riverton, OR 97015</p>
    <ul class="contacts">
      <li><svg viewBox="0 0 12 12"><path d="M3 1l2 2-1 1.5c.7 1.4 1.8 2.5 3.5 3.5L9 7l2 2-1.5 2C5 10.5 1.5 7 1 2.5z"/></svg>555.310.4827 <span class="contacts__label">Reception</span></li>
      <li><svg viewBox="0 0 12 12"><rect x="3" y="1" width="6" height="3"/><rect x="1" y="5" width="10" height="4"/><rect x="3" y="8" width="6" height="3"/></svg>555.310.4827 <span class="contacts__label">Fax</span></li>
      <li><svg viewBox="0 0 12 12"><path d="M1 3h10v6H1z M1 3l5 4 5-4" stroke="#111" stroke-width=".8"/></svg>info@marblecrest.com <span class="contacts__label">Reception</span></li>
      <li><svg viewBox="0 0 12 12"><path d="M1 3h10v6H1z M1 3l5 4 5-4" stroke="#111" stroke-width=".8"/></svg>daniel@marblecrest.com <span class="contacts__label">Direct</span></li>
      <li><svg viewBox="0 0 12 12"><circle cx="6" cy="6" r="5"/><path d="M1 6h10M6 1c2 2.5 2 7.5 0 10M6 1c-2 2.5-2 7.5 0 10" stroke="#111" stroke-width=".8" fill="none"/></svg>www.marblecrest.com</li>
    </ul>
  </div>
</section>

<section class="card card--back" aria-label="Card back">
  <div class="back__pattern" role="img" aria-label="Gloss-varnished repeating brand emblem pattern on black"></div>
  <div class="brand">
    <span class="brand__mark"></span>
    <span class="brand__rule"></span>
    <span class="brand__name">Marble Crest</span>
  </div>
</section>

</body>
</html>
```